Letterhead design for Dental Practice - Ashby Lane Dental Care

Letterhead for Private Dental Practice. To be used for all official correspondance and for printing treatment details on to be given to patients.

Target Market(s)

Private dental patients

Industry/Entity Type

Dental Clinic

Font styles to use
Other font styles liked:
• nexa-light

Colors
33a6d7
1c66ac
85abd2

Requirements
Must have
• info in the footer and header needs to be 3.5cm from upper/lower boader of paper, see photo in uploaded files
• info details:
• tel. 01632 960 418
• email info@ashbylanedc.co.uk
• ashbylanedentalcare.co.uk
• 17b Ashby Lane Fernbrook Eastholm ZZ2 7QT
• nexa-light font as in uploaded logo files
Should not have
• No funny tooth pictures

```html
<!DOCTYPE html>
<html lang="en">
<head>
<meta charset="utf-8">
<title>Ashby Lane Dental Care – Letterhead</title>
<link rel="stylesheet" href="https://fonts.googleapis.com/css2?family=Quicksand:wght@600&family=Source+Sans+3:wght@400;600&display=swap">
<style>
  :root {
    --brand-blue: #33a6d7;
    --brand-navy: #1c66ac;
    --brand-grey: #5a5a5c;
    --ink: #333335;
    --paper: #ffffff;
    --footer-text: #f2f2f2;
  }
  * { box-sizing: border-box; margin: 0; padding: 0; }
  html, body {
    width: 849px;
    height: 1200px;
    overflow: hidden;
    background: var(--paper);
  }
  .letterhead {
    position: relative;
    width: 849px;
    height: 1200px;
    background: var(--paper);
    font-family: "Source Sans 3", "Myriad Pro", sans-serif;
    color: var(--ink);
  }
  .brand {
    position: absolute;
    top: 110px;
    left: 0;
    width: 100%;
    display: flex;
    justify-content: center;
    align-items: center;
    gap: 10px;
  }
  .brand-mark {
    width: 12px;
    height: 12px;
    background: var(--brand-navy);
  }
  .brand-name {
    font-family: "Source Sans 3", sans-serif;
    font-weight: 600;
    font-size: 24px;
    letter-spacing: 0.3px;
    color: var(--brand-navy);
  }
  .recipient {
    position: absolute;
    top: 318px;
    left: 107px;
    font-style: normal;
    font-size: 16px;
    line-height: 21px;
  }
  .recipient .recipient-name { font-weight: 600; }
  .letter-body {
    position: absolute;
    top: 466px;
    left: 107px;
    width: 634px;
    font-size: 16px;
    line-height: 22px;
    text-align: justify;
    hyphens: auto;
  }
  .letter-body p + p { margin-top: 22px; }
  .sign-off {
    position: absolute;
    top: 808px;
    left: 107px;
    font-size: 16px;
    line-height: 21px;
  }
  .footer {
    position: absolute;
    left: 37px;
    top: 1124px;
    width: 776px;
    height: 44px;
  }
  .footer-shapes {
    position: absolute;
    inset: 0;
  }
  .footer-contact {
    position: absolute;
    left: 14px;
    top: 14px;
    height: 30px;
    display: flex;
    align-items: center;
    font-family: "Quicksand", sans-serif;
    font-weight: 600;
    font-size: 12.5px;
    color: var(--footer-text);
    white-space: nowrap;
  }
  .footer-divider {
    width: 1px;
    height: 16px;
    background: #9a9a9c;
    margin: 0 12px;
  }
  .footer-web {
    position: absolute;
    right: 18px;
    top: 7px;
    text-align: right;
    font-family: "Quicksand", sans-serif;
    font-weight: 600;
    font-size: 11.5px;
    line-height: 15px;
    color: var(--paper);
  }
</style>
</head>
<body>
<main class="letterhead">
  <header class="brand">
    <span class="brand-mark" aria-hidden="true"></span>
    <span class="brand-name">Ashby Lane Dental Care</span>
  </header>

  <address class="recipient">
    <div class="recipient-name">Name</div>
    <div>Title</div>
    <div>Address</div>
    <div>Postcode</div>
    <div>UK</div>
  </address>

  <section class="letter-body">
    <p>Lorem Ipsum is simply dummy vvvLorem ipsum dolor sit amet, consectetuer adipiscing elit, sed diam nonummy nibh euismod tincidunt ut laoreet dolore magna aliquam erat volutpat. Ut wisi enim ad minim veniam, quis nostrud exerci tation ullamcorper suscipit lobortis nisl ut aliquip ex ea commodo consequat. Duis autem vel eum iriure dolor in hendrerit in vulputate velit &nbsp;of Lorem Ipsum.</p>
    <p>Lorem ipsum dolor sit amet, consectetuer adipiscing elit, sed diam nonummy nibh euismod tincidunt ut laoreet dolore magna aliquam erat volutpat. Ut wisi enim ad minim veniam, quis nostrud exerci tation ullamcorper suscipit lobortis nisl ut aliquip ex ea commodo consequat. Duis autem vel eum iriure dolor in hendrerit in vulputate vel.</p>
    <p>Lorem ipsum dolor sit amet, consectetuer adipiscing elit.</p>
  </section>

  <div class="sign-off">
    <div>Name Here</div>
    <div>Signature</div>
  </div>

  <footer class="footer">
    <svg class="footer-shapes" width="776" height="44" viewBox="0 0 776 44" aria-hidden="true">
      <polygon points="0,14 530,14 520,44 0,44" fill="var(--brand-grey)"/>
      <polygon points="534,0 776,0 776,44 517,44" fill="var(--brand-blue)"/>
    </svg>
    <div class="footer-contact">
      <span>01632 960 418</span>
      <span class="footer-divider" aria-hidden="true"></span>
      <span>17b Ashby Lane Fernbrook Eastholm ZZ2 7QT</span>
    </div>
    <div class="footer-web">
      <div>ashbylanedentalcare.co.uk</div>
      <div>info@ashbylanedc.co.uk</div>
    </div>
  </footer>
</main>
</body>
</html>
```